Design & Content Treatments for small Tai Chi Teacher's Site

Wordpress is setup and ready to go. Really just need a header image (with text treatment of the site name and tag line), and really simple content treatments for each page (image selection and placement, etc). Ideally this will require very little modification to the actual wordpress template code.
Simpler is better. I will post images and am in the process of flowing all the text into the site now. If some sort of Iconic identity can be established Doug will be VERY happy, but it's not a requirement
Thank You!
Temporary Site URL is http://203.0.113.58/~pinecld4/
Final will be lanternharborstudioarts.com.

```html
<!DOCTYPE html>
<html lang="en">
<head>
<meta charset="utf-8">
<title>Lantern Harbor T'ai Chi</title>
<link rel="stylesheet" href="https://fonts.googleapis.com/css2?family=Raleway:wght@300&family=Open+Sans:wght@300;400;600&family=Arimo:wght@400&display=swap">
<style>
  :root {
    --page-top: #cfc8c1;
    --page-bottom: #e1dcd6;
    --panel: #ffffff;
    --ink: #2b2826;
    --text: #6f6a66;
    --nav-top: #5b5653;
    --nav-bottom: #383432;
    --nav-active: #2f2b29;
    --nav-line: #4a4543;
    --dropdown: rgba(58, 54, 52, 0.93);
    --caption-band: rgba(20, 18, 17, 0.72);
    --accent: #9c7a5a;
    --pill: #7d7470;
    --search-bg: #f4f1ee;
    --rule: #c9c4bf;
  }
  * { margin: 0; padding: 0; box-sizing: border-box; }
  html, body { width: 1200px; height: 1074px; overflow: hidden; }
  body {
    position: relative;
    background: linear-gradient(to bottom, var(--page-top) 0, var(--page-top) 477px, var(--page-bottom) 477px);
    font-family: "Open Sans", sans-serif;
  }
  .site {
    position: absolute; left: 42px; top: 31px; width: 1116px; height: 999px;
    background: var(--panel);
  }
  .site-title {
    position: absolute; left: 46px; top: 34px;
    font-family: "Raleway", sans-serif; font-weight: 300; font-size: 45px;
    color: var(--ink); letter-spacing: -0.5px; white-space: nowrap;
  }
  .search {
    position: absolute; left: 867px; top: 45px; width: 228px; height: 31px;
    background: var(--search-bg);
  }
  .search span {
    position: absolute; left: 10px; top: 7px; font-family: "Arimo", sans-serif;
    font-size: 13px; color: #c4beb9;
  }
  .search svg { position: absolute; right: 10px; top: 8px; }
  .main-nav {
    position: absolute; left: 13px; top: 128px; width: 1090px; height: 54px;
    background: linear-gradient(to bottom, var(--nav-top), var(--nav-bottom));
    display: flex; list-style: none;
  }
  .main-nav li {
    height: 54px; line-height: 54px; text-align: center;
    color: #fff; font-size: 15px; border-right: 1px solid var(--nav-line);
  }
  .main-nav li:last-child { border-right: none; }
  .main-nav li.active { background: var(--nav-active); }
  .submenu {
    position: absolute; left: 118px; top: 182px; width: 226px; height: 121px;
    background: var(--dropdown); list-style: none; padding-top: 12px; z-index: 2;
  }
  .submenu li { padding-left: 21px; height: 34px; line-height: 20px; color: #fff; font-size: 15px; }
  .hero {
    position: absolute; left: 13px; top: 182px; width: 1090px; height: 461px;
    background: linear-gradient(160deg, #b9a58c 0%, #8a6a4e 35%, #5b4a3d 60%, #9c6a40 100%);
  }
  .hero-caption {
    position: absolute; left: 0; top: 273px; width: 1090px; height: 149px;
    background: var(--caption-band); padding: 36px 0 0 38px;
    color: #fff; font-weight: 300; font-size: 30px; line-height: 39px;
  }
  .hero-caption em { font-style: italic; }
  .welcome { position: absolute; left: 30px; top: 666px; width: 680px; }
  .welcome h2, .upcoming h2 {
    font-family: "Arimo", sans-serif; font-weight: 400; font-size: 28px; color: var(--ink);
    margin-bottom: 6px;
  }
  .welcome p {
    font-family: "Arimo", sans-serif; font-size: 14px; line-height: 17.5px; color: var(--text);
    margin-bottom: 8px;
  }
  .welcome .read-more { display: block; margin-top: 14px; font-family: "Arimo", sans-serif; font-size: 14px; color: var(--accent); }
  .upcoming { position: absolute; left: 798px; top: 667px; width: 290px; }
  .pill {
    display: inline-block; background: var(--pill); color: #fff; border-radius: 10px;
    font-family: "Arimo", sans-serif; font-size: 12.5px; padding: 2px 12px; line-height: 16px;
  }
  .upcoming .pill { margin: 12px 0 0 2px; }
  .calendar {
    width: 280px; border-collapse: collapse; margin: 6px 0 0 2px;
    font-family: "Arimo", sans-serif; font-size: 14px; color: var(--text);
  }
  .calendar th { font-weight: 400; height: 26px; border-bottom: 1px solid var(--rule); width: 40px; }
  .calendar td { text-align: center; height: 22px; }
  .calendar tr:first-child td { padding-top: 3px; }
  .prev-month { margin: 6px 0 0 2px; }
  .site-footer {
    position: absolute; left: 0; top: 956px; width: 1116px; height: 43px;
    border-top: 1px dashed var(--rule);
    font-family: "Arimo", sans-serif; font-size: 14px; color: var(--text);
    padding: 12px 0 0 22px;
  }
</style>
</head>
<body>
  <div class="site">
    <header>
      <div class="site-title">Lantern Harbor T'ai Chi</div>
      <div class="search">
        <span>Search</span>
        <svg width="15" height="15" viewBox="0 0 15 15"><circle cx="6" cy="6" r="4.5" fill="none" stroke="#b9b2ac" stroke-width="2"/><line x1="9.5" y1="9.5" x2="13.5" y2="13.5" stroke="#b9b2ac" stroke-width="2.4" stroke-linecap="round"/></svg>
      </div>
      <ul class="main-nav">
        <li style="width:106px">Home</li>
        <li class="active" style="width:153px">Class Schedule</li>
        <li style="width:201px">About T'ai Chi Ch'uan</li>
        <li style="width:358px">Mentorship and Constructive Life Guidance</li>
        <li style="width:156px">Contact Doug</li>
        <li style="width:116px">Blog</li>
      </ul>
      <ul class="submenu">
        <li>Class Types &amp; Description</li>
        <li>Class Types &amp; Description</li>
        <li>Class Types &amp; Description</li>
      </ul>
    </header>

    <section class="hero" role="img" aria-label="Photo of a t'ai chi class practising together in a warm wood-floored studio">
      <div class="hero-caption">Group and Private T'ai Chi Ch'uan<br>Instruction by <em>Douglas Fairhurst</em></div>
    </section>

    <article class="welcome">
      <h2>Welcome</h2>
      <p>I am dedicated to sharing the profound and limitless potential of t'ai chi ch'uan as a method for self-healing – for achieving balance in all areas of life – and for the recovery of the optimum health and the integration of the body, mind and spirit.</p>
      <p>Inherent within t'ai chi, of course is it's martial function and it's potential for self-defense has been well documented and elucidated by numerous masters and adepts alike. Thus I will not treat the subject here, beyond to say that with daily practice over a period of time one will assuredly be able to defend oneself without a doubt.</p>
      <a class="read-more">Readmore »</a>
    </article>

    <aside class="upcoming">
      <h2>Upcoming Classes</h2>
      <span class="pill">April 2011</span>
      <table class="calendar">
        <thead><tr><th>S</th><th>M</th><th>T</th><th>W</th><th>T</th><th>F</th><th>S</th></tr></thead>
        <tbody>
          <tr><td></td><td></td><td></td><td></td><td></td><td>1</td><td>2</td></tr>
          <tr><td>3</td><td>4</td><td>5</td><td>6</td><td>7</td><td>8</td><td>9</td></tr>
          <tr><td>10</td><td>11</td><td>12</td><td>13</td><td>14</td><td>15</td><td>16</td></tr>
          <tr><td>17</td><td>18</td><td>19</td><td>20</td><td>21</td><td>22</td><td>23</td></tr>
          <tr><td>24</td><td>25</td><td>26</td><td>27</td><td>28</td><td>29</td><td>30</td></tr>
        </tbody>
      </table>
      <span class="pill prev-month">« Mar</span>
    </aside>

    <footer class="site-footer">© 2011 - Lantern Harbor T'ai Chi</footer>
  </div>
</body>
</html>
```